Brindle Works - Fast, Efficient and Gas Mainteance for Domestic, Commercial and Industrial clients

We are in the process of purchasing a new business and would like to get a new logo and business card.
Business is a gas maintenance business that also does new gas installations.
Has been established since 1988.
Services include:
Install all types of gas appliances & equipment inc. hot water units
Maintain / repair / replace all types of gas appliances & equipment

Target Market(s)

Domestic, Commercial and Industrial clients

Industry/Entity Type

Business

Contact Information for Business Card

admin@brindleworks-example.com.au
07 5981 4726
Brindle Works PTY LTD

Logo Text

Gas Fitting & Plumbing Maintenance Specialists

Font styles to use
Sans Serif

Requirements
Must have
• Logo
• Business name, contact number, email address, web address
• Domestic | Commercial | Industrial Est Since 1988
Nice to have
• Possibly a black card with a flame logo to one side
Should not have
• Spelling errors

```html
<!DOCTYPE html>
<html lang="en">
<head>
<meta charset="utf-8">
<title>Brindle Works – Business Card</title>
<link rel="stylesheet" href="https://fonts.googleapis.com/css2?family=Cinzel:wght@500&family=PT+Sans:wght@400&display=swap">
<style>
  :root {
    --backdrop: #ece6dc;
    --card-white: #ffffff;
    --brand-orange: #f48a35;
    --flame-yellow: #ffd23a;
    --flame-core: #fff3b0;
    --tagline-yellow: #ffe15a;
    --divider: #f7a866;
  }
  * { margin: 0; padding: 0; box-sizing: border-box; }
  html, body { width: 1200px; height: 569px; overflow: hidden; }
  body { background: var(--backdrop); position: relative; font-family: "PT Sans", sans-serif; }

  .card {
    position: absolute; top: 167px; width: 401px; height: 235px;
    border-radius: 12px; overflow: hidden;
    box-shadow: 0 3px 8px rgba(0,0,0,0.18);
  }
  .card--front { left: 175px; background: var(--card-white); }
  .card--back { left: 624px; background: var(--brand-orange); }

  .flame-area {
    position: absolute;
    background: radial-gradient(ellipse at 50% 60%, var(--flame-core) 0%, var(--flame-yellow) 40%, rgba(255,170,40,0.6) 70%, rgba(244,138,53,0) 100%);
  }

  /* Front */
  .name-band {
    position: absolute; left: 0; top: 92px; width: 325px; height: 62px;
    background: var(--brand-orange);
  }
  .name-band .flame-area { left: 0; top: 0; width: 72px; height: 62px; }
  .name-band__divider {
    position: absolute; left: 102px; top: 0; width: 1px; height: 62px; background: var(--divider);
  }
  .business-name {
    position: absolute; left: 113px; top: 13px;
    font-family: "Cinzel", serif; font-weight: 500; font-size: 19px;
    color: var(--card-white); letter-spacing: 0.3px; white-space: nowrap;
  }
  .tagline {
    position: absolute; left: 110px; top: 38px;
    font-size: 7.6px; color: var(--tagline-yellow); white-space: nowrap;
  }

  /* Back */
  .contact-band {
    position: absolute; left: 0; top: 92px; width: 324px; height: 63px;
    background: var(--card-white);
  }
  .card--back > .flame-area { left: 322px; top: 74px; width: 79px; height: 92px; }
  .contact-line {
    position: absolute; font-size: 9.5px; color: var(--brand-orange); white-space: nowrap;
  }
  .contact-line--email { right: 60px; top: 5px; }
  .contact-line--phone { right: 71px; top: 26px; }
  .contact-line--company { left: 156px; top: 44px; }
  .contact-icon { position: absolute; width: 13px; height: 10px; }
  .contact-icon--email { left: 263px; top: 7px; }
  .contact-icon--phone { left: 263px; top: 27px; }
</style>
</head>
<body>
  <section class="card card--front" aria-label="Business card front">
    <div class="name-band">
      <div class="flame-area" role="img" aria-label="Photograph of gas flames"></div>
      <div class="name-band__divider"></div>
      <h1 class="business-name">Brindle Works</h1>
      <p class="tagline">• Domestic • Commercial • Industrial Est Since 1988</p>
    </div>
  </section>

  <section class="card card--back" aria-label="Business card back">
    <div class="contact-band">
      <p class="contact-line contact-line--email">admin@brindleworks-example.com.au</p>
      <svg class="contact-icon contact-icon--email" viewBox="0 0 13 10" aria-hidden="true">
        <rect x="0" y="0" width="13" height="10" fill="var(--brand-orange)"/>
        <rect x="2.5" y="2" width="8" height="6" fill="none" stroke="#fff" stroke-width="0.9"/>
        <path d="M2.5 2 L6.5 5.5 L10.5 2" fill="none" stroke="#fff" stroke-width="0.9"/>
      </svg>
      <p class="contact-line contact-line--phone">07 5981 4726</p>
      <svg class="contact-icon contact-icon--phone" viewBox="0 0 13 10" aria-hidden="true">
        <rect x="0" y="0" width="13" height="10" fill="var(--brand-orange)"/>
        <rect x="4" y="1.5" width="5" height="7" rx="0.8" fill="none" stroke="#fff" stroke-width="0.9"/>
      </svg>
      <p class="contact-line contact-line--company">Brindle Works PTY LTD</p>
    </div>
    <div class="flame-area" role="img" aria-label="Photograph of gas flames"></div>
  </section>
</body>
</html>
```